Need 2 sided card for Loomfield Goods Co. Logo supplied.

I am looking for a business card for my online craft supply business.

I have a very simple design already which I am kind of happy with (see attached pdf) - but would like suggestions for something a little more creative. Design MUST be clean. Super clean! Think thin lines and not blocks of color...

Design must be clean and crisp. No other colors other than in palette (see link below)

I would also like to possible incorporate my tagline - maybe on the front but definitely on the back:
"HollowReed Ideas & Hobby Materials"

Logo file is supplied, but I think spacing on the card may required the wording to be moved underneaths the camera icon - which is fine. Font in logo is Maven Pro. OPEN TO USE OF OTHER FONTS ON CARD BUT MUST BE CLEAN DESIGN.

FRONT OF CARD
All information on attached pdf is correct and should be shown in your design.

BACK OF CARD
Needs to show www.tindalerow.example and maybe logo repeat and tagline.

SIZE
New Zealand sized - meaning finished card will be 90 x 55mm
Printing requirements: printed area is 90mm x 55mm with a 2mm bleed all round.

COLORS
Color palette used in logo can be seen here for HEX and RGB reference: http://www.huebankly.example/palette/8627410/website

NOTE: PAYMENT WILL BE MADE FOR THE BEST DESIGN - EVEN IF I DECIDE NOT TO USE IT.
Updates

Thank you all so much for your designs. I will be providing feedback to ALL designers tomorrow. This weekend is a holiday weekend here in New Zealand and so no work for a few days. Thank-you again - I appreciate your time and creativity!

Industry/Entity Type

Camera

Font styles to use
Other font styles liked:
• Maven Pro - open to others

Requirements
Must have
• Clean design. Logo must be prominent for brand recognition. All contact information must be shown.
Nice to have
• Tagline - at least on reverse

```html
<!DOCTYPE html>
<html lang="en">
<head>
<meta charset="utf-8">
<title>Loomfield Goods Co. – Business Card Concepts</title>
<link href="https://fonts.googleapis.com/css2?family=Maven+Pro:wght@400;500&family=Ubuntu:wght@400;500;700&display=swap" rel="stylesheet">
<style>
  :root{
    --mint:#dff5e8;
    --slate:#4a4f4e;
    --coral:#fb4a2b;
    --olive:#c8c419;
    --white:#ffffff;
    --trim:#555a59;
  }
  *{box-sizing:border-box;margin:0;padding:0}
  html,body{width:1200px;height:900px;overflow:hidden;background:#fff}
  body{position:relative;font-family:"Ubuntu",sans-serif;color:var(--slate)}

  .slot{position:absolute;width:375px;height:242px}
  .slot .crop{position:absolute;left:0;top:0;width:375px;height:242px}
  .crop line{stroke:var(--trim);stroke-width:1}
  .card{position:absolute;left:14px;top:14px;width:347px;height:214px;background:var(--mint);overflow:hidden;outline:1px solid var(--trim)}

  .brand{position:absolute;display:flex;flex-direction:column;align-items:center;text-align:center;font-family:"Maven Pro",sans-serif;font-weight:400;color:var(--slate);white-space:nowrap;line-height:1.05}
  .brand .dot{border-radius:50%;background:var(--olive);margin-bottom:6px}

  .name{position:absolute;font-weight:700;white-space:nowrap}
  .contact{position:absolute;list-style:none;font-size:10px;color:var(--white);letter-spacing:.1px}
  .contact li{display:flex;align-items:center;gap:4px;height:15px;white-space:nowrap}
  .ico{width:9px;height:9px;border-radius:50%;flex:none}

  /* front 1 */
  .f1 .band-name{position:absolute;left:0;top:107px;width:347px;height:23px;background:var(--coral);color:var(--white);font-size:15px;font-weight:700;text-align:center;line-height:23px}
  .f1 .panel{position:absolute;left:0;top:130px;width:347px;height:84px;background:var(--slate)}
  .f1 .ico{background:var(--coral)}

  /* front 2 */
  .f2{background:var(--slate)}
  .f2 .ico{background:var(--olive)}

  /* front 3 */
  .f3 .contact{font-size:12px}
  .f3 .contact li{position:absolute;height:auto;gap:8px}
  .f3 .ico{width:20px;height:20px;background:var(--mint);border:2px solid var(--slate);display:flex;align-items:center;justify-content:center}

  /* backs */
  .back .tagline{position:absolute;left:0;width:347px;top:145px;text-align:center;font-size:10.5px;font-weight:700;color:var(--coral);letter-spacing:.3px}
  .back .url-band{position:absolute;left:0;width:347px;top:180px;height:18px;color:var(--white);font-size:11.5px;text-align:center;line-height:18px;letter-spacing:.2px}
  .back .url-band.coral{background:var(--coral)}
  .back .url-band.slate{background:var(--slate)}
</style>
</head>
<body>

<!-- Front A -->
<div class="slot" style="left:26px;top:204px">
  <svg class="crop" viewBox="0 0 375 242"><line x1="0" y1="14" x2="10" y2="14"/><line x1="365" y1="14" x2="375" y2="14"/><line x1="0" y1="228" x2="10" y2="228"/><line x1="365" y1="228" x2="375" y2="228"/><line x1="14" y1="0" x2="14" y2="10"/><line x1="361" y1="0" x2="361" y2="10"/><line x1="14" y1="232" x2="14" y2="242"/><line x1="361" y1="232" x2="361" y2="242"/></svg>
  <div class="card f1">
    <div class="brand" style="left:0;width:347px;top:16px;font-size:21px"><span class="dot" style="width:44px;height:44px"></span>Loomfield Goods Co.</div>
    <div class="band-name">Maren Tolliver</div>
    <div class="panel"></div>
    <ul class="contact" style="left:17px;top:145px">
      <li><span class="ico"></span>+64 (0) 3 555 0142</li>
      <li><span class="ico"></span>+64 (0) 21 055 01938</li>
      <li><span class="ico"></span>m.tolliver@loomfieldnz.example</li>
    </ul>
    <ul class="contact" style="left:204px;top:145px">
      <li><span class="ico"></span>social.example/loomfield</li>
      <li><span class="ico"></span>www.tindalerow.example</li>
      <li><span class="ico"></span>www.loomfieldnz.example</li>
    </ul>
  </div>
</div>

<!-- Front B -->
<div class="slot" style="left:411px;top:204px">
  <svg class="crop" viewBox="0 0 375 242"><line x1="0" y1="14" x2="10" y2="14"/><line x1="365" y1="14" x2="375" y2="14"/><line x1="0" y1="228" x2="10" y2="228"/><line x1="365" y1="228" x2="375" y2="228"/><line x1="14" y1="0" x2="14" y2="10"/><line x1="361" y1="0" x2="361" y2="10"/><line x1="14" y1="232" x2="14" y2="242"/><line x1="361" y1="232" x2="361" y2="242"/></svg>
  <div class="card f2">
    <svg style="position:absolute;left:0;top:0" width="347" height="214" viewBox="0 0 347 214">
      <path d="M0 104 L94 14 Q100 8 106 14 L170 76 Q176 82 170 89 L47 214 L0 214 Z" fill="var(--mint)"/>
    </svg>
    <div class="brand" style="left:38px;width:120px;top:52px;font-size:13px"><span class="dot" style="width:28px;height:28px;margin-bottom:5px"></span>Loomfield<br>Goods Co.</div>
    <div class="name" style="left:212px;top:32px;font-size:14px;color:var(--olive);font-weight:500;letter-spacing:.5px">Maren Tolliver</div>
    <ul class="contact" style="left:161px;top:104px">
      <li><span class="ico"></span>+64 (0) 3 555 0142</li>
      <li><span class="ico"></span>+64 (0) 21 055 01938</li>
      <li><span class="ico"></span>m.tolliver@loomfieldnz.example</li>
      <li><span class="ico"></span>social.example/loomfield</li>
      <li><span class="ico"></span>www.tindalerow.example</li>
      <li><span class="ico"></span>www.loomfieldnz.example</li>
    </ul>
  </div>
</div>

<!-- Front C -->
<div class="slot" style="left:799px;top:204px">
  <svg class="crop" viewBox="0 0 375 242"><line x1="0" y1="14" x2="10" y2="14"/><line x1="365" y1="14" x2="375" y2="14"/><line x1="0" y1="228" x2="10" y2="228"/><line x1="365" y1="228" x2="375" y2="228"/><line x1="14" y1="0" x2="14" y2="10"/><line x1="361" y1="0" x2="361" y2="10"/><line x1="14" y1="232" x2="14" y2="242"/><line x1="361" y1="232" x2="361" y2="242"/></svg>
  <div class="card f3">
    <svg style="position:absolute;left:0;top:0" width="347" height="214" viewBox="0 0 347 214">
      <path d="M174 0 L347 0 L347 22 L210 22 L150 214 L104 214 Z" fill="var(--slate)"/>
      <path d="M210 22 L347 22 L347 214 L150 214 Z" fill="var(--coral)"/>
      <path d="M0 165 L130 165 L123 188 L0 188 Z" fill="var(--slate)"/>
    </svg>
    <div class="brand" style="left:10px;width:120px;top:26px;font-size:14px"><span class="dot" style="width:30px;height:30px;margin-bottom:5px"></span>Loomfield<br>Goods Co.</div>
    <div class="name" style="left:20px;top:169px;font-size:12.5px;color:var(--white)">Maren Tolliver</div>
    <ul class="contact">
      <li style="left:176px;top:31px"><span class="ico"><svg width="10" height="10" viewBox="0 0 10 10"><path d="M2 1 L4 1 L4.6 3 L3.4 4 Q4.3 5.8 6 6.6 L7 5.4 L9 6 L9 8 Q5 9 2.4 6.5 Q0.6 4 2 1Z" fill="var(--slate)"/></svg></span>+64 (0) 3 555 0142</li>
      <li style="left:167px;top:60px"><span class="ico"><svg width="8" height="11" viewBox="0 0 8 11"><rect x="1" y="0.5" width="6" height="10" rx="1" fill="none" stroke="var(--slate)" stroke-width="1.2"/></svg></span>+64 (0) 21 055 01938</li>
      <li style="left:158px;top:88px;font-size:9px"><span class="ico"><svg width="11" height="8" viewBox="0 0 11 8"><rect x="0.5" y="0.5" width="10" height="7" fill="none" stroke="var(--slate)"/><path d="M0.5 0.5 L5.5 4.5 L10.5 0.5" fill="none" stroke="var(--slate)"/></svg></span>m.tolliver@loomfieldnz.example</li>
      <li style="left:149px;top:117px"><span class="ico"></span>social.example/loomfield</li>
      <li style="left:140px;top:145px"><span class="ico"></span>www.tindalerow.example</li>
      <li style="left:131px;top:174px"><span class="ico"><svg width="11" height="11" viewBox="0 0 11 11"><circle cx="5.5" cy="5.5" r="4.8" fill="none" stroke="var(--slate)"/><path d="M0.7 5.5 H10.3 M5.5 0.7 V10.3" stroke="var(--slate)"/></svg></span>www.loomfieldnz.example</li>
    </ul>
  </div>
</div>

<!-- Back A -->
<div class="slot" style="left:26px;top:453px">
  <svg class="crop" viewBox="0 0 375 242"><line x1="0" y1="14" x2="10" y2="14"/><line x1="365" y1="14" x2="375" y2="14"/><line x1="0" y1="228" x2="10" y2="228"/><line x1="365" y1="228" x2="375" y2="228"/><line x1="14" y1="0" x2="14" y2="10"/><line x1="361" y1="0" x2="361" y2="10"/><line x1="14" y1="232" x2="14" y2="242"/><line x1="361" y1="232" x2="361" y2="242"/></svg>
  <div class="card back">
    <div class="brand" style="left:0;width:347px;top:30px;font-size:26px"><span class="dot" style="width:58px;height:58px;margin-bottom:10px"></span>Loomfield Goods Co.</div>
    <div class="tagline">HollowReed Ideas &amp; Hobby Materials</div>
    <div class="url-band coral">www.tindalerow.example</div>
  </div>
</div>

<!-- Back B -->
<div class="slot" style="left:411px;top:453px">
  <svg class="crop" viewBox="0 0 375 242"><line x1="0" y1="14" x2="10" y2="14"/><line x1="365" y1="14" x2="375" y2="14"/><line x1="0" y1="228" x2="10" y2="228"/><line x1="365" y1="228" x2="375" y2="228"/><line x1="14" y1="0" x2="14" y2="10"/><line x1="361" y1="0" x2="361" y2="10"/><line x1="14" y1="232" x2="14" y2="242"/><line x1="361" y1="232" x2="361" y2="242"/></svg>
  <div class="card back">
    <div class="brand" style="left:0;width:347px;top:30px;font-size:26px"><span class="dot" style="width:58px;height:58px;margin-bottom:10px"></span>Loomfield Goods Co.</div>
    <div class="tagline">HollowReed Ideas &amp; Hobby Materials</div>
    <div class="url-band slate">www.tindalerow.example</div>
  </div>
</div>

<!-- Back C -->
<div class="slot" style="left:799px;top:449px">
  <svg class="crop" viewBox="0 0 375 242"><line x1="0" y1="14" x2="10" y2="14"/><line x1="365" y1="14" x2="375" y2="14"/><line x1="0" y1="228" x2="10" y2="228"/><line x1="365" y1="228" x2="375" y2="228"/><line x1="14" y1="0" x2="14" y2="10"/><line x1="361" y1="0" x2="361" y2="10"/><line x1="14" y1="232" x2="14" y2="242"/><line x1="361" y1="232" x2="361" y2="242"/></svg>
  <div class="card back">
    <div class="brand" style="left:0;width:347px;top:34px;font-size:26px"><span class="dot" style="width:58px;height:58px;margin-bottom:10px"></span>Loomfield Goods Co.</div>
    <div class="tagline" style="top:149px">HollowReed Ideas &amp; Hobby Materials</div>
    <div class="url-band slate">www.tindalerow.example</div>
  </div>
</div>

</body>
</html>
```